Harbor Learning Center Posters Showing Building Blocks

We need poster designs for a School in Arizona for kids with Autism. There will be 4 such posters needed which highlight our schools building blocks. Requirements for all 4 posters are as followed: 1) We need the Harbor Learning Center Logo on each poster. I have included attachment. 2) The posters need the following titles: Building Block #1 (for the first poster), Building Block #2 for the 2nd poster, Building Block #3 for the 3rd poster, and Building Block #4 for the forth poster. 3) The main text and focus of the posters will be the following key words: For the first poster the words "Kids first in every decision". The words for the second poster are: "Students are friends with each other, and welcome new students with open arms." The words for the 3rd poster are: "The school is quiet, and students are working hard to do their best." The words for the 4th poster are: "Parents see amazing improvement in their child." 4) We would love to use some of the kids art from our schools if possible. Use your expertise to decide. I will send these out as well. 5) Try and design the posters around the key words from each poster 6) I am sure if landscape or portrait would be best so I will let the experts decide. All 4 posters need to be the same layout once decided.

Target Market(s)

These posters are for the school only. Prospective students/parents will see these posters so they will be used for Marketing from that perspective. We may put out into local community in future.

Industry/Entity Type

School

Font styles to use
Serif

Requirements
Must have
• 1) Logo (Harbor Learning Center for Growth and Discovery)
• 2) Title: as described in write up
• 3) Key words: as described in write up
Nice to have
• Kids art from school. Note: This is the first time that I have been on this site so I may have made a mistake by putting 4 posters on one project. I am assuming that I would need to pay more to have 4 posters so let me know if I need to modify the project in any way?

```html
<!DOCTYPE html>
<html lang="en">
<head>
<meta charset="utf-8">
<title>School Building Block #1 — Kids first in every decision</title>
<link rel="stylesheet" href="https://fonts.googleapis.com/css2?family=Alegreya+SC:wght@700&family=Gochi+Hand&display=swap">
<style>
  :root {
    --paper: #ffffff;
    --plum: #8a3a78;
    --sun: #fff200;
    --sun-tag: #fdf23a;
    --cloud: #e3e4e5;
    --ink: #1a1a1a;
    --art-pink: #ec8fb7;
    --art-blue: #2f5fa6;
    --art-green: #7cc242;
    --art-orange: #f29a2e;
  }
  * { box-sizing: border-box; margin: 0; padding: 0; }
  html, body { width: 848px; height: 1200px; overflow: hidden; background: var(--paper); }
  .poster { position: relative; width: 848px; height: 1200px; background: var(--paper); overflow: hidden; }

  .title-banner {
    position: absolute; left: 72px; top: 30px; width: 698px; height: 128px;
  }
  .title-banner svg { position: absolute; inset: 0; }
  .title-banner h1 {
    position: absolute; inset: 0;
    display: flex; align-items: center; justify-content: center;
    padding-bottom: 24px;
    font-family: "Alegreya SC", Georgia, serif; font-weight: 700;
    font-size: 70px; letter-spacing: 1px; color: var(--sun);
  }
  .block-tag {
    position: absolute; left: 305px; top: 140px; width: 228px; height: 66px;
    background: var(--sun-tag);
    box-shadow: 3px 4px 5px rgba(0,0,0,0.25);
    transform: rotate(-0.6deg);
    display: flex; align-items: center; justify-content: center;
    font-family: "Alegreya SC", Georgia, serif; font-weight: 700;
    font-size: 38px; color: var(--plum); letter-spacing: 1px;
  }

  .value-cloud { position: absolute; left: 48px; top: 290px; width: 760px; height: 712px; }
  .value-cloud svg { position: absolute; inset: 0; }

  .student-art {
    position: absolute; left: 528px; top: 325px; width: 240px; height: 565px;
    border-radius: 110px 110px 36px 36px;
    background: linear-gradient(180deg, var(--art-blue) 0%, var(--art-blue) 17%, var(--art-pink) 22%, var(--art-orange) 52%, var(--art-pink) 68%, var(--art-green) 100%);
    box-shadow: 4px 5px 6px rgba(0,0,0,0.25);
  }

  .key-words {
    position: absolute; left: 112px; top: 405px; width: 400px;
    z-index: 2;
    font-family: "Gochi Hand", "Comic Sans MS", cursive;
    color: var(--ink); transform: rotate(-3deg); transform-origin: left top;
  }
  .key-words span { display: block; line-height: 0.95; white-space: nowrap; }
  .kw-kids { font-size: 124px; }
  .kw-first { font-size: 100px; margin-left: 48px; }
  .kw-every { font-size: 90px; margin-left: -14px; }
  .kw-decision { font-size: 94px; margin-left: 20px; }

  .school-mark {
    position: absolute; left: 278px; top: 1052px;
    display: flex; align-items: center; gap: 12px;
    font-family: "Alegreya SC", Georgia, serif; font-weight: 700; color: var(--ink);
  }
  .school-mark .mark-square { width: 38px; height: 38px; background: var(--plum); }
  .school-mark .mark-name { font-size: 21px; line-height: 1.2; }
</style>
</head>
<body>
<main class="poster">
  <header class="title-banner">
    <svg width="698" height="128" viewBox="0 0 698 128" aria-hidden="true">
      <path d="M4 8 L180 2 L420 6 L694 0 L690 40 L696 90 L692 128 L500 122 L250 126 L2 124 L6 80 L0 40 Z" fill="var(--plum)"/>
    </svg>
    <h1>School Building</h1>
  </header>
  <div class="block-tag">Block #1</div>

  <section class="value-cloud">
    <svg width="760" height="712" viewBox="0 0 760 712" aria-hidden="true">
      <path d="M60 70 C160 20 330 10 520 8 C640 6 740 40 752 200 C760 360 758 520 720 620 C680 700 520 712 340 706 C180 700 60 690 24 600 C0 480 8 300 14 180 C18 120 30 90 60 70 Z" fill="var(--cloud)"/>
    </svg>
  </section>

  <div class="student-art" role="img" aria-label="Cut-out child figure painted by a student in blue, pink, orange and green swirls"></div>

  <p class="key-words">
    <span class="kw-kids">Kids</span>
    <span class="kw-first">first</span>
    <span class="kw-every">in every</span>
    <span class="kw-decision">decision!</span>
  </p>

  <footer class="school-mark">
    <span class="mark-square"></span>
    <span class="mark-name">Harbor Learning Center<br>for Growth and Discovery</span>
  </footer>
</main>
</body>
</html>
```